Business Card Design

I want a simple and modern design, but also something very catching to the eye.

Also is there anyway that the text can be adjusted or changed so that I may make cards for other employees? If so, please make it so that I may edit the texts at a future date.

Reason: I need all designers to update the business card with my update information.

Industry/Entity Type

Business

Contact Information for Business Card

Owner: Marcus Halvorsen
Company Name: Play Brixo
Phone # :555-203-7841
Website: playbrixoshop.example
Email: marc@playbrixoshop.example

```html
<!DOCTYPE html>
<html lang="en">
<head>
<meta charset="utf-8">
<title>Play Brixo – Business Card</title>
<link rel="stylesheet" href="https://fonts.googleapis.com/css2?family=Prompt:wght@300;400;600&family=Open+Sans:wght@400&display=swap">
<style>
  :root {
    --frame-cyan: #00aeef;
    --card-white: #ffffff;
    --band-navy: #2e3192;
    --name-navy: #262262;
    --title-red: #ed1c24;
    --contact-teal: #1aa99a;
    --brand-navy: #262262;
  }
  * { margin: 0; padding: 0; box-sizing: border-box; }
  html, body {
    width: 1200px;
    height: 686px;
    overflow: hidden;
    background: var(--frame-cyan);
  }
  .card {
    position: relative;
    width: 1200px;
    height: 686px;
    background: var(--frame-cyan);
    font-family: "Prompt", sans-serif;
  }
  .card__panel {
    position: absolute;
    left: 45px;
    top: 45px;
    width: 1110px;
    height: 555px;
    background: var(--card-white);
  }
  .card__band {
    position: absolute;
    left: 0;
    top: 600px;
    width: 1200px;
    height: 48px;
    background: var(--band-navy);
  }
  .brand {
    position: absolute;
    left: 118px;
    top: 350px;
    display: flex;
    align-items: center;
    gap: 18px;
  }
  .brand__mark {
    width: 58px;
    height: 58px;
    background: var(--frame-cyan);
  }
  .brand__name {
    font-family: "Prompt", sans-serif;
    font-weight: 600;
    font-size: 68px;
    line-height: 1;
    color: var(--brand-navy);
    white-space: nowrap;
  }
  .person__name,
  .person__role,
  .contact__line,
  .website {
    position: absolute;
    line-height: 1;
    white-space: nowrap;
  }
  .person__name {
    left: 602px;
    top: 266px;
    font-weight: 300;
    font-size: 46px;
    color: var(--name-navy);
    letter-spacing: 0.5px;
  }
  .person__role {
    left: 754px;
    top: 318px;
    font-weight: 300;
    font-size: 34px;
    color: var(--title-red);
  }
  .contact__line {
    left: 602px;
    font-weight: 300;
    color: var(--contact-teal);
  }
  .contact__line--phone { top: 445px; font-size: 39px; }
  .contact__line--email { top: 508px; font-size: 30px; left: 604px; }
  .website {
    left: 678px;
    top: 608px;
    font-family: "Open Sans", sans-serif;
    font-weight: 400;
    font-size: 27px;
    color: var(--card-white);
  }
</style>
</head>
<body>
  <main class="card">
    <div class="card__panel"></div>
    <div class="card__band"></div>

    <div class="brand">
      <span class="brand__mark"></span>
      <span class="brand__name">Play Brixo</span>
    </div>

    <p class="person__name">Marcus Halvorsen</p>
    <p class="person__role">Owner</p>

    <p class="contact__line contact__line--phone">Phone : 555-203-7841</p>
    <p class="contact__line contact__line--email">Email : marc@playbrixoshop.example</p>

    <p class="website">Website : playbrixoshop.example</p>
  </main>
</body>
</html>
```